Tarnowicz Family website redesign

Our family website tarnowicz.com has not been updated since 2010 and desperately needs a new look that's easy to edit. The new design needs to be able to accommodate all the current sections (some text, some photos/images/gallery), although not all need to be listed in top-level tabs.

The feel of the design should be fun and colorful without being childish or cartoonish (we're almost 60!). Also, we are math and engineering types so generally prefer geometric patterns/graphics.

I've attached some logos, graphics, and business card (done through ArtHarbor) that we use in other ways and especially like the green/red hummingbird, if it can be incorporated somehow.

Target Market(s)

Family and personal friends

Font styles to use
Sans Serif

Colors

Designer to choose colors to be used in the design.

Requirements
Must have
• Photo galleries, Contact Us form, password-protected section or page-by-page
Nice to have
• Blog posts (not sure we will use this but would be nice to have the option); social media links (Friendbook, Snapgram, Chirper)
Should not have
• E-commerce

```html
<!DOCTYPE html>
<html lang="en">
<head>
<meta charset="utf-8">
<title>Anna &amp; Teo — Tarnowicz Family</title>
<link href="https://fonts.googleapis.com/css2?family=Montserrat:wght@500;600;700;800;900&family=Open+Sans:wght@400;600&display=swap" rel="stylesheet">
<style>
:root{
  --green:#24520f;
  --blue:#1b4f9e;
  --red:#c8171c;
  --ink:#111;
  --text:#333;
  --soft:#f3efef;
  --blush:#ecd3d3;
  --footer:#232323;
  --white:#fff;
}
*{box-sizing:border-box;margin:0;padding:0}
html,body{width:1200px;height:3797px;overflow:hidden;background:var(--white)}
body{font-family:"Open Sans",Arial,sans-serif;color:var(--text)}
.page{position:relative;width:1200px;height:3797px;overflow:hidden}
.abs{position:absolute}
.btn{position:absolute;background:var(--green);color:var(--white);font:700 13px "Montserrat",sans-serif;letter-spacing:.5px;text-transform:uppercase;display:flex;align-items:center;justify-content:center}
.heading{position:absolute;left:0;width:1200px;text-align:center;font:800 32px "Montserrat",sans-serif;color:var(--ink);text-transform:uppercase}
.heading::after{content:"";display:block;width:56px;height:3px;background:#bbb;margin:18px auto 0}

/* header */
.site-header{left:0;top:0;width:1200px;height:122px;background:var(--white);z-index:2}
.brand{left:152px;top:-10px;width:190px;height:182px;border-radius:50%;background:var(--white);z-index:3;display:flex;align-items:flex-end;justify-content:center;padding-bottom:44px}
.brand span{font:700 25px "Montserrat",sans-serif;color:var(--green)}
.follow{left:730px;top:36px;font:700 11px "Montserrat",sans-serif;color:var(--ink);display:flex;gap:8px;align-items:center}
.follow i{display:block;width:26px;height:26px;border-radius:50%;background:var(--blue)}
.search{left:934px;top:30px;width:122px;height:30px;border:1px solid #ccc;font-size:10px;color:#999;padding:8px 10px}
.search svg{position:absolute;right:8px;top:9px}
.nav{left:442px;top:80px;display:flex;font:700 12.5px "Montserrat",sans-serif;color:var(--ink)}
.nav a{padding:7px 14px;text-transform:uppercase}
.nav a.active{background:var(--green);color:var(--white)}

/* hero */
.hero{left:0;top:122px;width:1200px;height:580px;
  background:
    radial-gradient(ellipse 260px 340px at 90px 260px,#5f7f3c 0%,transparent 70%),
    radial-gradient(ellipse 240px 320px at 1130px 240px,#6a8a45 0%,transparent 70%),
    radial-gradient(ellipse 520px 300px at 600px 520px,#1c1d26 0%,transparent 75%),
    linear-gradient(180deg,#6b7a58 0%,#4a5a3a 40%,#2b2c2c 100%)}
.hero-title{left:0;top:404px;width:1200px;text-align:center;color:var(--white);font:800 30px/1.3 "Montserrat",sans-serif;text-transform:uppercase}
.hero-title strong{display:block;font-size:46px;font-weight:900}
.dots{display:flex;gap:14px;justify-content:center;align-items:center}
.dots i{width:9px;height:9px;border-radius:50%;background:#fff}
.dots i.on{background:transparent;border:2px solid #fff;width:13px;height:13px}

/* about */
.about{left:0;top:689px;width:1200px;height:570px;background:var(--soft)}
.about-mark{left:24px;top:210px;width:220px;font:700 34px/1.2 "Montserrat",sans-serif;color:var(--blush)}
.about h2{left:220px;top:100px;font:800 32px "Montserrat",sans-serif;color:var(--ink);text-transform:uppercase}
.about .rule{left:220px;top:148px;width:110px;height:3px;background:#bbb}
.about p{position:absolute;left:220px;width:360px;font-size:15px;line-height:1.65;color:var(--text)}

/* tiles */
.tile{top:1253px;width:400px;height:350px}
.tile-label{position:absolute;left:24px;bottom:18px;color:var(--white);font:800 19px "Montserrat",sans-serif;text-transform:uppercase}
.tile-go{position:absolute;right:22px;bottom:14px;width:34px;height:34px;border-radius:50%;background:var(--red)}
.tile-go svg{display:block}

/* what's new */
.news-card{top:1780px;width:224px;height:188px;border:1px solid #ccc;background:var(--white)}
.news-card .date{position:absolute;left:-4px;top:18px;background:var(--blue);color:#fff;font:700 10px "Montserrat",sans-serif;padding:6px 10px}
.news-card p{position:absolute;left:30px;top:66px;width:172px;font-size:12px;line-height:1.45;color:var(--text)}
.news-card .btn{left:30px;top:136px;width:84px;height:26px;font-size:9.5px}

/* gallery */
.gallery{left:0;top:2096px;width:1200px;height:583px;background:repeating-linear-gradient(135deg,#f1eded 0 14px,#ebe6e6 14px 15px)}
.shot{top:2272px;width:241px;height:222px;border:5px solid #fff;box-shadow:0 2px 6px rgba(0,0,0,.2)}
.caption{top:2510px;width:241px;text-align:center;font:600 14px/1.3 "Montserrat",sans-serif;color:var(--ink);text-transform:uppercase}
.arrow-box{top:2360px;width:40px;height:40px;background:var(--blue)}

/* blog */
.post{top:2861px;width:286px;height:433px;background:#fff;box-shadow:0 3px 12px rgba(0,0,0,.18)}
.post .photo{position:absolute;left:0;top:0;width:286px;height:233px}
.post .date{position:absolute;left:22px;top:222px;background:var(--blue);color:#fff;font:700 11px "Montserrat",sans-serif;padding:7px 12px}
.post h3{position:absolute;left:40px;top:266px;width:215px;font:700 17px/1.25 "Montserrat",sans-serif;color:var(--ink)}
.post p{position:absolute;left:40px;top:318px;width:215px;font-size:12px;line-height:1.5;color:var(--text)}
.post .btn{left:40px;top:380px;width:96px;height:30px;font-size:10px}

/* footer */
.footer{left:0;top:3372px;width:1200px;height:425px;background:var(--footer);color:#ccc}
.foot-brand{left:148px;top:100px;font:700 24px "Montserrat",sans-serif;color:var(--green);display:flex;align-items:center;gap:12px}
.foot-brand i{width:18px;height:18px;background:var(--red);border-radius:50%}
.foot-col h4{font:700 12px "Montserrat",sans-serif;color:#fff;text-transform:uppercase;margin-bottom:22px}
.foot-col li{list-style:none;font-size:12px;line-height:1.55}
.contact li{display:flex;gap:14px;margin-bottom:16px}
.contact svg{flex:none;margin-top:2px}
.social li{display:flex;align-items:center;gap:12px;margin-bottom:14px}
.social i{width:26px;height:26px;border-radius:50%;background:var(--blue);display:block}
.foot-rule{left:148px;top:325px;width:904px;height:1px;background:#3a3a3a}
.copyright{left:0;top:372px;width:1200px;text-align:center;font-size:11px;color:#bbb}
</style>
</head>
<body>
<div class="page">

  <header class="site-header abs">
    <div class="follow abs">FOLLOW US : <i></i><i></i><i></i></div>
    <div class="search abs">SEARCH<svg width="11" height="11" viewBox="0 0 11 11"><circle cx="4.5" cy="4.5" r="3.5" stroke="#333" stroke-width="1.6" fill="none"/><path d="M7 7l3 3" stroke="#333" stroke-width="1.6"/></svg></div>
    <nav class="nav abs">
      <a class="active">Home</a><a>Christmas Cards</a><a>Kids</a><a>What's New</a><a>Fun &amp; Games</a><a>Gallery</a><a>Admin</a>
    </nav>
  </header>
  <div class="brand abs"><span>Anna &amp; Teo</span></div>

  <section class="hero abs" role="img" aria-label="Family portrait of six people in formal clothes standing in a garden"></section>
  <div class="hero-title abs">Welcome to<strong>Anna &amp; Teo</strong></div>
  <div class="btn" style="left:531px;top:528px;width:138px;height:40px;background:var(--blue)">Read More</div>
  <div class="dots abs" style="left:0;top:622px;width:1200px"><i></i><i></i><i class="on"></i><i></i><i></i></div>
  <svg class="abs" style="left:0;top:670px" width="1200" height="30" viewBox="0 0 1200 30" preserveAspectRatio="none">
    <polygon fill="var(--soft)" points="0,18 60,12 130,20 210,10 300,19 380,13 470,21 560,11 650,18 740,12 830,20 920,10 1010,18 1100,12 1200,19 1200,30 0,30"/>
  </svg>

  <section class="about abs">
    <div class="about-mark abs">Anna &amp; Teo</div>
    <h2 class="abs">About Us</h2>
    <div class="rule abs"></div>
    <p style="top:182px">All of our Christmas picture cards (starting in the year we were married, 1981) are now available. All Holiday letters (starting in 1989) are now available.</p>
    <p style="top:300px">Only Hit Counter visitors since January 1, 2010. Definitely not enough to make it to the top 10 in web traffic.</p>
    <div class="btn" style="left:222px;top:423px;width:124px;height:40px">Read More</div>
    <svg class="abs" style="left:625px;top:58px" width="420" height="470" viewBox="0 0 420 470">
      <defs>
        <linearGradient id="house" x1="0" y1="0" x2="0" y2="1">
          <stop offset="0" stop-color="#e4e9ef"/><stop offset=".3" stop-color="#4a4f3a"/><stop offset=".55" stop-color="#9a5a45"/><stop offset=".8" stop-color="#5b3a30"/><stop offset="1" stop-color="#2f4a2a"/>
        </linearGradient>
      </defs>
      <polygon fill="var(--blue)" points="225,20 405,120 405,340 225,445 45,340 45,120"/>
      <polygon fill="url(#house)" role="img" aria-label="Red brick family house with white columns and trees" points="205,0 385,100 385,320 205,425 25,320 25,100"/>
    </svg>
  </section>

  <div class="tile abs" style="left:0;background:linear-gradient(180deg,#8fa6c4 0%,#b7b3a6 30%,#7a7466 60%,#4b4436 100%)" role="img" aria-label="Couple sitting on a granite mountain overlook">
    <span class="tile-label">Christmas Cards</span><span class="tile-go"><svg width="34" height="34"><path d="M15 11l6 6-6 6" stroke="#fff" stroke-width="2.5" fill="none"/></svg></span></div>
  <div class="tile abs" style="left:400px;background:radial-gradient(ellipse 160px 190px at 210px 150px,#c9a377,transparent 70%),linear-gradient(180deg,#b99a5c,#7a5a30 60%,#2e2418)" role="img" aria-label="Vintage portrait of a young man in glasses">
    <span class="tile-label">Kids</span><span class="tile-go"><svg width="34" height="34"><path d="M15 11l6 6-6 6" stroke="#fff" stroke-width="2.5" fill="none"/></svg></span></div>
  <div class="tile abs" style="left:800px;background:linear-gradient(180deg,#9fb4d4 0%,#dfe3ea 35%,#c9ccd6 55%,#3c3f6a 85%,#2a2b45 100%)" role="img" aria-label="Family in ski gear on a snowy slope">
    <span class="tile-label">Fun &amp; Games</span><span class="tile-go"><svg width="34" height="34"><path d="M15 11l6 6-6 6" stroke="#fff" stroke-width="2.5" fill="none"/></svg></span></div>

  <h2 class="heading" style="top:1668px">What's New</h2>
  <div class="news-card abs" style="left:144px"><span class="date">12/14/03</span><p>Christmas card and holiday letter for 2003 now available.</p><span class="btn">Read More</span></div>
  <div class="news-card abs" style="left:375px"><span class="date">12/19/03</span><p>TJ's photo album from our June 2002 China trip.</p><span class="btn">Read More</span></div>
  <div class="news-card abs" style="left:605px"><span class="date">10/23/03</span><p>My mother passed away today.</p><span class="btn">Read More</span></div>
  <div class="news-card abs" style="left:835px"><span class="date">10/02/03</span><p>Added a few new cartoons.</p><span class="btn">Read More</span></div>
  <div class="abs" style="left:543px;top:2012px;display:flex;gap:7px;align-items:center">
    <span style="color:#999;font-size:12px">‹</span>
    <i style="width:8px;height:8px;border-radius:50%;background:var(--red)"></i>
    <i style="width:8px;height:8px;border-radius:50%;background:#ccc"></i><i style="width:8px;height:8px;border-radius:50%;background:#ccc"></i>
    <i style="width:8px;height:8px;border-radius:50%;background:#ccc"></i><i style="width:8px;height:8px;border-radius:50%;background:#ccc"></i>
    <i style="width:8px;height:8px;border-radius:50%;background:#ccc"></i>
    <span style="color:#999;font-size:12px">›</span>
  </div>

  <section class="gallery abs"></section>
  <h2 class="heading" style="top:2152px">Photo Gallery</h2>
  <div class="arrow-box abs" style="left:0"><svg width="40" height="40"><path d="M23 13l-7 7 7 7" stroke="#fff" stroke-width="2.5" fill="none"/></svg></div>
  <div class="arrow-box abs" style="left:1160px"><svg width="40" height="40"><path d="M17 13l7 7-7 7" stroke="#fff" stroke-width="2.5" fill="none"/></svg></div>
  <div class="shot abs" style="left:78px;background:linear-gradient(180deg,#2f4f98 0%,#5a6ea6 45%,#8a7a6a 70%,#c49a4a 100%)" role="img" aria-label="Family playing a board game at a table"></div>
  <div class="shot abs" style="left:347px;background:linear-gradient(180deg,#e0dbd0 0%,#8a7a66 40%,#4a3c34 70%,#2a2a2a 100%)" role="img" aria-label="Family group on a staircase"></div>
  <div class="shot abs" style="left:613px;background:linear-gradient(180deg,#6a3e2a 0%,#b04a3a 50%,#a83232 75%,#2f6b38 100%)" role="img" aria-label="Holiday photo collage at a new home"></div>
  <div class="shot abs" style="left:884px;background:linear-gradient(180deg,#8c97b0 0%,#55566a 40%,#2a2a36 100%)" role="img" aria-label="Family in formal wear at an event"></div>
  <div class="caption abs" style="left:78px">Happy Holiday to You</div>
  <div class="caption abs" style="left:347px">Happy Holidays</div>
  <div class="caption abs" style="left:613px">Happy Holidays<br>From Our New Home</div>
  <div class="caption abs" style="left:884px">Holiday Letter</div>
  <div class="btn" style="left:512px;top:2580px;width:176px;height:40px">View All Images</div>

  <h2 class="heading" style="top:2745px">Latest Blog</h2>
  <article class="post abs" style="left:144px">
    <div class="photo" style="background:linear-gradient(180deg,#9aa69a 0%,#7d8a76 35%,#c9382f 70%,#8a2a24 100%)" role="img" aria-label="Couple on the Great Wall"></div>
    <span class="date">29 Nov, 2018</span><h3>Lorem Ipsum is simply dummy text</h3>
    <p>It is a long established fact that a reader will be distracted by the readable content.</p><span class="btn">Read More</span>
  </article>
  <article class="post abs" style="left:456px">
    <div class="photo" style="background:linear-gradient(180deg,#cfc9bd 0%,#6a635a 40%,#2a2a2a 100%)" role="img" aria-label="Couple holding a baby"></div>
    <span class="date">29 Nov, 2018</span><h3>Lorem Ipsum is simply dummy text</h3>
    <p>It is a long established fact that a reader will be distracted by the readable content.</p><span class="btn">Read More</span>
  </article>
  <article class="post abs" style="left:770px">
    <div class="photo" style="background:linear-gradient(180deg,#9fb0c4 0%,#a98a6c 40%,#4a4a52 75%,#6a6a70 100%)" role="img" aria-label="Couple on a city street"></div>
    <span class="date">29 Nov, 2018</span><h3>Lorem Ipsum is simply dummy text</h3>
    <p>It is a long established fact that a reader will be distracted by the readable content.</p><span class="btn">Read More</span>
  </article>

  <svg class="abs" style="left:0;top:3350px" width="1200" height="24" viewBox="0 0 1200 24" preserveAspectRatio="none">
    <polygon fill="var(--footer)" points="0,12 50,6 120,14 190,4 270,13 350,7 430,15 520,5 600,12 690,6 780,14 860,4 950,12 1040,6 1120,14 1200,8 1200,24 0,24"/>
  </svg>
  <footer class="footer abs">
    <div class="foot-brand abs"><i></i>Anna &amp; Teo</div>
    <div class="foot-col contact abs" style="left:446px;top:108px;width:260px">
      <h4>Contact Us</h4>
      <ul>
        <li><svg width="12" height="14" viewBox="0 0 12 14"><path d="M6 0a5 5 0 0 1 5 5c0 4-5 9-5 9S1 9 1 5a5 5 0 0 1 5-5z" fill="#ccc"/><circle cx="6" cy="5" r="2" fill="#232323"/></svg><span>Lindenhoflaan 24<br>4811 KB Breda, The Netherlands</span></li>
        <li><svg width="12" height="12" viewBox="0 0 12 12"><path d="M2 0l3 3-1.5 2a7 7 0 0 0 3.5 3.5L9 7l3 3-2 2C5 12 0 7 0 2z" fill="#ccc"/></svg><span>999.999.9999</span></li>
        <li><svg width="13" height="10" viewBox="0 0 13 10"><rect width="13" height="10" fill="#ccc"/><path d="M0 0l6.5 5L13 0" stroke="#232323" fill="none"/></svg><span>info@tarnowicz.com</span></li>
      </ul>
    </div>
    <div class="foot-col abs" style="left:760px;top:108px">
      <h4>Menu</h4>
      <ul><li>Home</li><li>Christmas Cards</li><li>Kids</li><li>What's New</li><li>Fun &amp; Games</li><li>Photo Album</li><li>Admin</li></ul>
    </div>
    <div class="foot-col social abs" style="left:939px;top:108px">
      <h4>Connect With Us</h4>
      <ul><li><i></i>Friendbook</li><li><i></i>Chirper</li><li><i></i>Snapgram</li></ul>
    </div>
    <div class="foot-rule abs"></div>
    <div class="copyright abs">Copyrights © 2018 All Rights Reserved</div>
  </footer>

</div>
</body>
</html>
```